Criminal Defense Lawyer needs Website
Venturo Law Office
Criminal Defense Lawyer needs Website - Law
Creative Brief
Law
venturolawoffice.com
Ned Venturo of Venturo Law Office is dedicated exclusively to the practice of criminal law. Areas of Practice: DUI Felony Charges Misdemeanor Charges Criminal Record Expungements Driver's License Reinstatement Traffic Tickets
below header
http://telbrolaw.com
http://wdmlaw.com
http://www.pelvanostrick.com
I am looking for a cutting edge design. welcome screen should be more visual than informative. It should be a portal to each individual sub-page. please refer to my current website, venturolawoffice.com, for content related information. I would like the same secondary pages as my current site: attorney profile, legal services, duo, etc... I would like a website that is simple yet cutting edge on the welcome screen. It needs to incorporate my logo and one of the full or three quarter body portraits i have included. do not include the close up or casual photo on the welcome screen; those are reserved for the attorney profile page. feel free to use a background fill on the portraits if necessary. please be creative on menu navigation. CREATIVE MENU DESIGN ON THE WELCOME SCREEN IS A MUST!
moomtaz moomtaz
Designers, Thank you for your designs. I will pick a winner in the next few days after consulting my staff.
I understand that other concepts are veiled. The following websites have what I consider creative and dynamic menu design: http://www.q-vlaw.com http://dornaklawllc.com http://farquist-firm.com
Designers, Please submit some welcome page designs incorporating photo entitled 2015_Ned_Venturo_Business_Portraits_8_51884.jpg Would like to see full body length and 3/4 length versions. Thank you.
I like the unconventional menu design in #20 and #22. That is the type of creative menu I discussed in my brief.
Just to let designers know, during the first few days of the contest I will be giving three stars to designs that appeal to mE. This will let all designers know where to concentrate the designs. Closer to the end of the contest I will upgrade the finalists to four and five stars. I will give feedback to certain designs throughout the contest if I need specific changes. Please refer to my brief for a general approach. Some have done this, others have not.

```html
<!DOCTYPE html>
<html lang="en">
<head>
<meta charset="utf-8">
<title>Venturo Law Office</title>
<link rel="stylesheet" href="https://fonts.googleapis.com/css2?family=Oswald:wght@400;600&family=Open+Sans:wght@400;600&display=swap">
<style>
  :root {
    --bg: #0c0907;
    --brown-deep: #1a0f08;
    --brown-warm: #6b3e1e;
    --cream: #f1e6d4;
    --muted: #b9aa96;
    --faint: #8a7f72;
    --panel: #17120e;
    --panel-edge: #3a2f27;
    --pill-top: #545454;
    --pill-bottom: #1b1b1b;
    --accent: #c8262a;
    --white: #ffffff;
  }
  * { box-sizing: border-box; margin: 0; padding: 0; }
  html, body { width: 1200px; height: 919px; overflow: hidden; }
  body {
    position: relative;
    background: var(--bg);
    font-family: "Open Sans", Arial, sans-serif;
    color: var(--muted);
  }
  .header-scene {
    position: absolute; left: 0; top: 0; width: 1200px; height: 390px;
    background:
      radial-gradient(ellipse 520px 300px at 78% 30%, var(--brown-warm), transparent 70%),
      radial-gradient(ellipse 420px 260px at 22% 20%, #4a2a14, transparent 70%),
      linear-gradient(180deg, var(--brown-deep) 0%, var(--bg) 100%);
  }
  .brand {
    position: absolute; left: 308px; top: 14px;
    display: flex; align-items: center; gap: 10px;
  }
  .brand-dot { width: 34px; height: 34px; border-radius: 50%; background: var(--cream); }
  .brand-name {
    font-family: "Oswald", Arial, sans-serif; font-weight: 600;
    font-size: 22px; color: var(--cream); letter-spacing: 1px;
  }
  .contact {
    position: absolute; left: 752px; top: 10px; text-align: right; width: 150px;
    font-size: 10px; line-height: 14px; color: var(--cream);
  }
  .contact .phone { font-family: "Oswald", Arial, sans-serif; font-size: 15px; line-height: 20px; }
  .main-nav {
    position: absolute; left: 318px; top: 68px; width: 583px; height: 22px;
    display: flex; border-bottom: 1px solid var(--panel-edge);
  }
  .main-nav a {
    font-size: 11px; color: var(--muted); text-decoration: none;
    padding: 3px 14px; line-height: 16px; white-space: nowrap;
  }
  .main-nav a.active { color: var(--white); margin-left: 76px; border-bottom: 2px solid var(--accent); }
  .hero {
    position: absolute; left: 318px; top: 100px; width: 583px; height: 256px;
    border: 1px solid var(--panel-edge); border-radius: 4px; overflow: hidden;
    background: linear-gradient(180deg, #2a1d14, #0f0b08);
    box-shadow: 0 10px 30px rgba(0,0,0,.7);
  }
  .hero-portrait {
    position: absolute; left: 0; top: 0; width: 290px; height: 256px;
    background: radial-gradient(ellipse at 50% 40%, #6d5a4c, #2a1e16 75%);
  }
  .hero-copy { position: absolute; left: 300px; top: 52px; width: 270px; color: var(--white); }
  .hero-copy .kicker { font-family: "Oswald", Arial, sans-serif; font-size: 20px; line-height: 24px; }
  .hero-copy h1 { font-family: "Oswald", Arial, sans-serif; font-weight: 600; font-size: 29px; line-height: 34px; white-space: nowrap; }
  .hero-copy h2 { font-family: "Oswald", Arial, sans-serif; font-weight: 400; font-size: 16px; line-height: 20px; margin-bottom: 8px; white-space: nowrap; }
  .hero-copy p { font-size: 9.5px; line-height: 13px; color: var(--muted); margin-bottom: 12px; }
  .btn {
    display: inline-block; font-size: 10px; color: var(--white);
    background: linear-gradient(180deg, var(--pill-top), var(--pill-bottom));
    border: 1px solid #666; border-radius: 3px; padding: 4px 14px; white-space: nowrap;
  }
  .hero-copy .btn { padding: 6px 22px; }
  .slide-dot { position: absolute; left: 922px; top: 337px; width: 8px; height: 8px; border-radius: 50%; background: var(--accent); }
  .practice-heading {
    position: absolute; left: 0; top: 396px; width: 1200px; text-align: center;
    font-family: "Oswald", Arial, sans-serif; color: var(--white);
  }
  .practice-heading .title { font-size: 19px; letter-spacing: 3px; line-height: 22px; }
  .practice-heading .sub { font-size: 11px; letter-spacing: 2px; color: var(--cream); }
  .practice-grid {
    position: absolute; left: 354px; top: 443px; width: 522px;
    display: grid; grid-template-columns: repeat(3, 166px); gap: 14px 12px;
  }
  .practice-card {
    position: relative; height: 92px; border-radius: 6px;
    border: 1px solid var(--panel-edge);
    background: linear-gradient(180deg, #211a15, #0d0a08);
  }
  .practice-card h3 {
    margin: 4px; height: 24px; border-radius: 12px;
    background: linear-gradient(180deg, var(--pill-top), var(--pill-bottom));
    border: 1px solid #6a6a6a;
    font-family: "Oswald", Arial, sans-serif; font-weight: 400; font-size: 12px;
    color: var(--white); text-align: center; line-height: 22px;
    white-space: nowrap; overflow: hidden;
  }
  .practice-card h3.compact { font-size: 9.5px; letter-spacing: -0.1px; }
  .practice-card p { font-size: 8px; line-height: 11px; color: var(--faint); padding: 3px 10px; text-align: center; }
  .practice-card .btn { position: absolute; right: 6px; bottom: 5px; font-size: 7px; padding: 1px 6px; }
  .welcome { position: absolute; left: 344px; top: 668px; width: 260px; }
  .section-title { font-family: "Oswald", Arial, sans-serif; font-size: 16px; color: var(--white); letter-spacing: 1px; line-height: 20px; white-space: nowrap; }
  .video {
    margin-top: 12px; width: 246px; height: 76px; border: 1px solid var(--panel-edge);
    background: linear-gradient(90deg, #2b1f17, #5a4536 60%, #1c140f);
  }
  .welcome p { font-size: 8px; line-height: 11px; color: var(--faint); margin-top: 12px; width: 230px; }
  .social { display: flex; gap: 5px; margin-top: 28px; }
  .social span { width: 22px; height: 22px; border-radius: 3px; background: #3b3b3b; }
  .social span:nth-child(odd) { background: #555; }
  .footer-links { position: absolute; left: 344px; top: 888px; font-size: 7.5px; color: var(--faint); white-space: nowrap; }
  .blog { position: absolute; left: 637px; top: 668px; width: 262px; }
  .post { display: flex; gap: 14px; margin-top: 12px; }
  .post:first-of-type { margin-top: 16px; }
  .date { width: 30px; text-align: center; font-family: "Oswald", Arial, sans-serif; color: var(--white); }
  .date b { display: block; font-size: 20px; line-height: 22px; font-weight: 600; }
  .date small { display: block; font-size: 9px; line-height: 11px; }
  .post-text { font-size: 8.5px; line-height: 12px; color: var(--cream); }
  .post-text .meta { color: var(--faint); font-size: 7.5px; }
  .post-text .meta em { color: var(--accent); font-style: normal; }
  .blog > .btn { position: absolute; left: 185px; top: 166px; font-size: 8px; padding: 2px 12px; }
  .cards { position: absolute; left: 778px; top: 884px; display: flex; gap: 4px; }
  .cards span { width: 26px; height: 16px; border-radius: 2px; background: #d8d2c8; }
  .cards span:nth-child(2) { background: #9a9088; }
  .cards span:nth-child(3) { background: #c4bcb0; }
  .cards span:nth-child(4) { background: #8f877d; }
</style>
</head>
<body>
  <div class="header-scene" role="img" aria-label="Dark warm-toned photo of a wooden judge's gavel"></div>

  <div class="brand">
    <span class="brand-dot"></span>
    <span class="brand-name">VENTURO LAW OFFICE</span>
  </div>

  <div class="contact">
    418 W. Marrow St., Suite 3<br>
    Linden, IL 62000<br>
    <span class="phone">217-555-0148</span>
  </div>

  <nav class="main-nav">
    <a class="active" href="#">Home</a>
    <a href="#">Attorney Profile</a>
    <a href="#">Legal Services</a>
    <a href="#">Resources</a>
    <a href="#">Contact Us</a>
  </nav>

  <section class="hero">
    <div class="hero-portrait" role="img" aria-label="Three-quarter portrait of attorney Ned Venturo in a dark suit"></div>
    <div class="hero-copy">
      <div class="kicker">WELCOME TO</div>
      <h1>VENTURO LAW OFFICE</h1>
      <h2>NED VENTURO - ATTORNEY AT LAW</h2>
      <p>Ned Venturo of Venturo Law Office is dedicated exclusively to the practice of criminal law. From DUI and felony charges to traffic tickets, he offers clear counsel and strong defense at every stage of your case.</p>
      <span class="btn">Read More</span>
    </div>
  </section>
  <span class="slide-dot"></span>

  <div class="practice-heading">
    <div class="title">CRIMINAL DEFENSE</div>
    <div class="sub">AREAS OF PRACTICE</div>
  </div>

  <div class="practice-grid">
    <article class="practice-card"><h3>DUI</h3><p>Clear answers and firm defense for every charge you face in court. Call today to talk about your case.</p><span class="btn">More</span></article>
    <article class="practice-card"><h3>FELONY CHARGES</h3><p>Clear answers and firm defense for every charge you face in court. Call today to talk about your case.</p><span class="btn">More</span></article>
    <article class="practice-card"><h3>MISDEMEANOR CHARGES</h3><p>Clear answers and firm defense for every charge you face in court. Call today to talk about your case.</p><span class="btn">More</span></article>
    <article class="practice-card"><h3 class="compact">CRIMINAL RECORD EXPUNGEMENTS</h3><p>Clear answers and firm defense for every charge you face in court. Call today to talk about your case.</p><span class="btn">More</span></article>
    <article class="practice-card"><h3 class="compact">DRIVER'S LICENSE REINSTATEMENT</h3><p>Clear answers and firm defense for every charge you face in court. Call today to talk about your case.</p><span class="btn">More</span></article>
    <article class="practice-card"><h3>TRAFFIC TICKETS</h3><p>Clear answers and firm defense for every charge you face in court. Call today to talk about your case.</p><span class="btn">More</span></article>
  </div>

  <section class="welcome">
    <div class="section-title">WELCOME TO VENTURO</div>
    <div class="video" role="img" aria-label="Video still of the attorney beside the office name"></div>
    <p>Meet the attorney and learn how our office handles criminal cases from first call to final verdict.</p>
    <div class="social"><span></span><span></span><span></span><span></span><span></span></div>
  </section>
  <div class="footer-links">Home | Attorney Profile | Legal Services | Resources | Contact Us</div>

  <section class="blog">
    <div class="section-title">LATEST BLOG POST</div>
    <div class="post">
      <div class="date"><b>22</b><small>OCT</small></div>
      <div class="post-text">New Illinois DUI rules take effect this month<br><span class="meta">Posted in <em>News</em> | 3 Comments</span></div>
    </div>
    <div class="post">
      <div class="date"><b>17</b><small>OCT</small></div>
      <div class="post-text">What to expect at a driver's license hearing<br><span class="meta">Posted in <em>Licenses</em> | 2 Comments</span></div>
    </div>
    <div class="post">
      <div class="date"><b>11</b><small>OCT</small></div>
      <div class="post-text">How record expungement can clear your past<br><span class="meta">Posted in <em>Records</em> | 1 Comment</span></div>
    </div>
    <span class="btn">Read More</span>
  </section>
  <div class="cards"><span></span><span></span><span></span><span></span></div>
</body>
</html>
```